Accounting Practice Business Card Design

I have a logo I am happy for you to use in the design of the Business Card.
You can edit and change colours as you please, I am not fixated on it.
I am looking for a modern and clean overall feel for the finished design.

The business is a small accounting practice who thrives on word of mouth referrals and this card will be given to all current and prospect clients.

Industry/Entity Type

Accountant

Contact Information for Business Card

Marcus Vell
Level 5, 8 Ashcombe Ridge Road
FERNMOOR RISE VIC 3187
Phone: 9481 3052
Email: mvell@qrnaccountants.com.au
Web: www.qrnaccountants.com.au

Font styles to use
Serif
Sans Serif

Colors
0555a3
3277b5
85acd3
0393ce
33a6d7
85cae6
00a990
33b8a4
9bcb3c

Requirements
Must have
• "The end to your tax problems begin with us"
• "A referral from you is our greatest compliment"
Nice to have
• Modern clean professional

```html
<!DOCTYPE html>
<html lang="en">
<head>
<meta charset="utf-8">
<title>QRN Accountants – Business Card</title>
<link rel="stylesheet" href="https://fonts.googleapis.com/css2?family=Arimo:wght@400;700&display=swap">
<style>
  :root {
    --brand-blue: #0a4f95;
    --brand-green: #3c7d1e;
    --card-white: #f7f7f7;
    --panel-text: #e8eef6;
    --page-bg: #e6e6e6;
    --card-radius: 18px;
  }
  * { margin: 0; padding: 0; box-sizing: border-box; }
  html, body {
    width: 1200px; height: 997px; overflow: hidden;
    background: var(--page-bg);
    font-family: "Arimo", Arial, sans-serif;
  }
  .sheet {
    position: relative; width: 1200px; height: 997px;
    display: flex; flex-direction: column; align-items: center;
    justify-content: center; gap: 56px;
  }
  .card {
    position: relative; width: 700px; height: 400px;
    border-radius: var(--card-radius); overflow: hidden;
    background: var(--card-white);
    box-shadow: 0 6px 22px rgba(0,0,0,.18);
  }
  .wordmark__name {
    display: block; font-weight: 700; color: var(--brand-blue);
    line-height: 1.05; text-transform: uppercase; white-space: nowrap;
  }

  /* Logo side */
  .card--logo .wordmark {
    position: absolute; left: 0; right: 0; top: 140px; text-align: center;
  }
  .card--logo .wordmark__name { font-size: 56px; letter-spacing: 2px; }
  .card--logo .referral {
    position: absolute; left: 0; right: 0; bottom: 46px;
    text-align: center; font-size: 16px; letter-spacing: 2px;
    text-transform: uppercase; color: var(--brand-blue); white-space: nowrap;
  }
  .referral__emph { color: var(--brand-green); }

  /* Contact side */
  .card--contact { display: flex; }
  .card--contact .edge-stripe { width: 10px; background: var(--brand-green); flex: none; }
  .card--contact .brand-area {
    position: relative; width: 370px; flex: none; background: var(--card-white);
  }
  .brand-area .wordmark { position: absolute; left: 36px; top: 112px; }
  .brand-area .wordmark__name { font-size: 40px; letter-spacing: 1px; }
  .slogan {
    position: absolute; left: 36px; bottom: 66px;
    text-transform: uppercase; white-space: nowrap;
  }
  .slogan__lead {
    display: block; color: var(--brand-blue);
    font-size: 15px; letter-spacing: 1.4px;
  }
  .slogan__close {
    display: block; color: var(--brand-green); font-weight: 700;
    font-size: 19px; letter-spacing: 3px; margin-top: 8px; padding-left: 62px;
  }
  .card--contact .divider-stripe { width: 12px; flex: none; background: var(--brand-green); }
  .contact-panel {
    flex: 1; background: var(--brand-blue); color: var(--panel-text);
    padding: 42px 28px 0 20px; text-align: right; position: relative;
  }
  .person__name {
    font-weight: 700; font-size: 18px; letter-spacing: 1px;
    text-transform: uppercase;
  }
  .person__role { font-size: 12px; margin-top: 3px; }
  .address { margin-top: 54px; font-size: 14px; line-height: 1.45; }
  .reach { position: absolute; right: 28px; bottom: 52px; font-size: 14px; }
  .reach__row {
    display: flex; align-items: center; justify-content: flex-end;
    gap: 10px; height: 28px; white-space: nowrap;
  }
  .reach__icon { width: 18px; height: 18px; flex: none; }
</style>
</head>
<body>
<main class="sheet">

  <section class="card card--logo" aria-label="Card back">
    <div class="wordmark"><span class="wordmark__name">QRN Accountants</span></div>
    <p class="referral">A referral from you is <span class="referral__emph">our greatest compliment</span></p>
  </section>

  <section class="card card--contact" aria-label="Card front">
    <div class="edge-stripe"></div>
    <div class="brand-area">
      <div class="wordmark">
        <span class="wordmark__name">QRN</span>
        <span class="wordmark__name">Accountants</span>
      </div>
      <p class="slogan">
        <span class="slogan__lead">The end to your tax problems</span>
        <span class="slogan__close">Begin with us</span>
      </p>
    </div>
    <div class="divider-stripe"></div>
    <div class="contact-panel">
      <p class="person__name">Marcus Vell</p>
      <p class="person__role">Managing Director</p>
      <p class="address">Level 5, 8 Ashcombe Ridge Road<br>Fernmoor Rise Vic 3187</p>
      <div class="reach">
        <div class="reach__row">
          <span>9481 3052</span>
          <svg class="reach__icon" viewBox="0 0 18 18" aria-hidden="true">
            <circle cx="9" cy="9" r="9" fill="#e8eef6"/>
            <path d="M5.5 4.5l2 .2.6 2.2-1.1 1a6 6 0 0 0 3 3l1-1.1 2.2.6.2 2c-4.6.6-8.5-3.3-7.9-7.9z" fill="#0a4f95"/>
          </svg>
        </div>
        <div class="reach__row">
          <span>mvell@qrnaccountants.com.au</span>
          <svg class="reach__icon" viewBox="0 0 18 18" aria-hidden="true">
            <circle cx="9" cy="9" r="9" fill="#e8eef6"/>
            <rect x="4.5" y="6" width="9" height="6.2" fill="#0a4f95"/>
            <path d="M4.8 6.3L9 9.4l4.2-3.1" stroke="#e8eef6" stroke-width=".9" fill="none"/>
          </svg>
        </div>
        <div class="reach__row">
          <span>www.qrnaccountants.com.au</span>
          <svg class="reach__icon" viewBox="0 0 18 18" aria-hidden="true">
            <circle cx="9" cy="9" r="9" fill="#e8eef6"/>
            <circle cx="9" cy="9" r="4.6" fill="none" stroke="#0a4f95" stroke-width="1.1"/>
            <path d="M4.4 9h9.2M9 4.4c-2.4 2.6-2.4 6.6 0 9.2M9 4.4c2.4 2.6 2.4 6.6 0 9.2" stroke="#0a4f95" stroke-width=".9" fill="none"/>
          </svg>
        </div>
      </div>
    </div>
  </section>

</main>
</body>
</html>
```